New Modern floristry business design

Hi, we are a new business based in Sydney called "velvet moss floristry"

With so many floristry's we need a good design that will set a great first impression.

A few descriptive words on how we envision velvet moss floristry:

-dynamic design
-minimal colour (colour can be used to enhance the design)
-black white grey (can include gold,silver,metallic shadowing)
Strong "VELVET MOSS" with a classy "FLORISTRY"
Bold with a touch of feminine

Industry/Entity Type

Business

Contact Information for Business Card

Velvet Moss Floristry,
Delphine Ruvek,
Velvetmossfloristry@quillmail.com.au

```html
<!DOCTYPE html>
<html lang="en">
<head>
<meta charset="utf-8">
<title>Velvet Moss Floristry – Business Cards</title>
<link rel="stylesheet" href="https://fonts.googleapis.com/css2?family=Cinzel:wght@400;700&family=Tinos&display=swap">
<style>
  :root {
    --backdrop: #dcdcdc;
    --card-dark: #1c1c1c;
    --card-deep: #101010;
    --band-grey: #565656;
    --ink-light: #ececec;
    --rule: #d4d4d4;
    --leaf-tone: rgba(205, 205, 205, 0.55);
  }
  * { box-sizing: border-box; margin: 0; padding: 0; }
  html, body {
    width: 1200px;
    height: 1000px;
    overflow: hidden;
    background: var(--backdrop);
  }
  .canvas {
    position: relative;
    width: 1200px;
    height: 1000px;
  }
  .card {
    position: absolute;
    width: 732px;
    height: 442px;
    overflow: hidden;
    color: var(--ink-light);
  }
  .card--front {
    left: 35px;
    top: 32px;
    background: linear-gradient(to bottom,
      var(--card-dark) 0, var(--card-dark) 80px,
      var(--band-grey) 112px, var(--band-grey) 320px,
      var(--card-deep) 350px, var(--card-deep) 100%);
  }
  .card--back {
    left: 401px;
    top: 527px;
    background: linear-gradient(to bottom,
      var(--card-dark) 0, #262626 150px,
      var(--band-grey) 180px, var(--band-grey) 300px,
      var(--card-deep) 330px, var(--card-deep) 100%);
  }
  .leaf-motif {
    position: absolute;
    background: radial-gradient(ellipse at center, var(--leaf-tone) 0, rgba(205,205,205,0.35) 45%, rgba(205,205,205,0) 72%);
  }
  .card--front .leaf-motif { left: 185px; top: 23px; width: 360px; height: 395px; }
  .card--back .leaf-motif { left: 159px; top: 23px; width: 390px; height: 400px; }
  .line {
    position: absolute;
    left: 0;
    width: 100%;
    text-align: center;
    white-space: nowrap;
  }
  .brand-name {
    font-family: "Cinzel", serif;
    font-weight: 700;
  }
  .card--front .brand-name { top: 130px; font-size: 60px; letter-spacing: 2px; }
  .card--back .brand-name { top: 40px; font-size: 40px; letter-spacing: 1px; }
  .brand-rule {
    position: absolute;
    height: 2px;
    background: var(--rule);
  }
  .card--front .brand-rule { left: 73px; width: 578px; top: 214px; }
  .card--back .brand-rule { left: 167px; width: 390px; top: 96px; }
  .brand-sub {
    font-family: "Cinzel", serif;
    font-weight: 400;
  }
  .card--front .brand-sub { top: 250px; font-size: 38px; letter-spacing: 4px; }
  .card--back .brand-sub { top: 368px; font-size: 30px; letter-spacing: 3px; }
  .person-name {
    top: 180px;
    font-family: "Cinzel", serif;
    font-weight: 700;
    font-size: 50px;
    letter-spacing: 1px;
  }
  .contact-email {
    top: 250px;
    font-family: "Tinos", serif;
    font-size: 26px;
  }
</style>
</head>
<body>
<main class="canvas">
  <section class="card card--front" aria-label="Business card front">
    <div class="leaf-motif" role="img" aria-label="Large pale maple leaf decoration"></div>
    <p class="line brand-name">VELVET MOSS</p>
    <div class="brand-rule"></div>
    <p class="line brand-sub">Floristry</p>
  </section>

  <section class="card card--back" aria-label="Business card back">
    <div class="leaf-motif" role="img" aria-label="Large pale maple leaf decoration"></div>
    <p class="line brand-name">VELVET MOSS</p>
    <div class="brand-rule"></div>
    <p class="line person-name">DELPHINE RUVEK</p>
    <p class="line contact-email">Velvetmossfloristry@quillmail.com.au</p>
    <p class="line brand-sub">Floristry</p>
  </section>
</main>
</body>
</html>
```